Book Cover for Willow Kindred Notes from the Meadow

We have written a book that brings together Notes from the Meadow from a variety of women's voices.
We developed a draft book cover that we like using Canva (attached below). We'd love a book cover that is similar to this image, but looks more professional.
Following are the themes we’d like to depict in the book cover, and in parentheses, how they are represented in the current cover:
1. Divinely feminine (overall cover)
2. Currents of enlightenment (the swirls of light carrying the butterfly)
3. Diversity (a myriad of colors)
4. The solo journey into the unknown (the single butterfly’s flight)
5. Buoyancy and joy (again, the dancing colors and floating butterfly)
6. Boldly feminine (the blue butterfly, set against brush strokes of light)
7. Homage to a dear friend (she loved blue butterflies, the cosmos - this butterfly has hints of the cosmos in her wings, and painting - this background has brush strokes of light).
Book Title, Subtitle, and Editor:
Willow Kindred
Notes from the Meadow
Edited by Mirela Tove
Thank you very much for considering this project!
People who are interested in Women and Spirituality

```html
<!DOCTYPE html>
<html lang="en">
<head>
<meta charset="utf-8">
<title>Willow Kindred — Notes from the Meadow</title>
<link rel="stylesheet" href="https://fonts.googleapis.com/css2?family=Kanit:wght@600;700&family=Allura&display=swap">
<style>
  :root {
    --stage: #e6e6e4;
    --cover-blue: #2160ec;
    --cover-deep: #1a4fdc;
    --glow-cyan: #3fdcf2;
    --glow-mid: #3896f0;
    --title-white: #ffffff;
    --script-navy: #1b2ab4;
    --wing-violet: #3a2ec8;
    --wing-blue: #2a78ea;
    --wing-sky: #4aa6f4;
    --wing-cream: #efe2b4;
  }
  * { margin: 0; padding: 0; box-sizing: border-box; }
  html, body {
    width: 1200px;
    height: 733px;
    overflow: hidden;
    background: var(--stage);
  }
  .stage {
    width: 1200px;
    height: 733px;
    display: flex;
    align-items: center;
    justify-content: center;
  }
  .book-cover {
    position: relative;
    width: 489px;
    height: 733px;
    overflow: hidden;
    background:
      radial-gradient(ellipse 42% 34% at 55% 42%, var(--glow-cyan) 0%, var(--glow-mid) 40%, rgba(33,96,236,0) 78%),
      linear-gradient(180deg, var(--cover-blue) 0%, var(--cover-deep) 100%);
  }
  .title {
    position: absolute;
    left: 50px;
    top: 26px;
    font-family: "Kanit", sans-serif;
    font-weight: 700;
    font-size: 96px;
    line-height: 80px;
    letter-spacing: -1px;
    color: var(--title-white);
    text-transform: uppercase;
  }
  .title span { display: block; }
  .subtitle {
    position: absolute;
    left: 48px;
    top: 172px;
    width: 390px;
    font-family: "Allura", cursive;
    color: var(--script-navy);
  }
  .subtitle-lead {
    display: block;
    text-align: right;
    font-size: 42px;
    line-height: 42px;
  }
  .subtitle-main {
    display: block;
    font-size: 100px;
    line-height: 84px;
    margin-top: -6px;
    letter-spacing: 2px;
  }
  .butterfly-art {
    position: absolute;
    left: 74px;
    top: 272px;
    width: 364px;
    height: 358px;
  }
  .byline {
    position: absolute;
    left: 0;
    right: 0;
    top: 646px;
    text-align: center;
    font-family: "Kanit", sans-serif;
    font-weight: 600;
    font-size: 35px;
    letter-spacing: 0.2px;
    color: var(--title-white);
    text-transform: uppercase;
  }
</style>
</head>
<body>
<main class="stage">
  <section class="book-cover">
    <h1 class="title"><span>Willow</span><span>Kindred</span></h1>
    <p class="subtitle">
      <span class="subtitle-lead">Notes from the</span>
      <span class="subtitle-main">Meadow</span>
    </p>
    <svg class="butterfly-art" viewBox="0 0 364 358" role="img" aria-label="Photograph of a single blue and violet butterfly with cream-banded wings, spread in flight">
      <defs>
        <radialGradient id="wingTone" cx="48%" cy="56%" r="52%">
          <stop offset="0%" stop-color="var(--wing-cream)" stop-opacity="0.95"/>
          <stop offset="22%" stop-color="var(--wing-sky)" stop-opacity="0.95"/>
          <stop offset="55%" stop-color="var(--wing-blue)" stop-opacity="0.95"/>
          <stop offset="85%" stop-color="var(--wing-violet)" stop-opacity="0.9"/>
          <stop offset="100%" stop-color="var(--wing-violet)" stop-opacity="0"/>
        </radialGradient>
      </defs>
      <ellipse cx="182" cy="190" rx="180" ry="168" fill="url(#wingTone)"/>
    </svg>
    <p class="byline">Edited by Mirela Tove</p>
  </section>
</main>
</body>
</html>
```